New Advertising Company Business Card

A two sided business card. One side with logo only and the other side with my information and maybe my logo again. Looking for something unique and creative, but not too busy. Info would include my name(Marcus Feldon), President, phone number, address, email address, and website. LOGO IS THE BLUE AND WHITE ONE.

Target Market(s)

CEO/VP Level Audience

Industry/Entity Type

Business

Contact Information for Business Card

In Description.

```html
<!DOCTYPE html>
<html lang="en">
<head>
<meta charset="utf-8">
<title>Harbor Advertising – Business Card</title>
<link rel="stylesheet" href="https://fonts.googleapis.com/css2?family=Arimo:wght@700&family=Lato:wght@400&family=Montserrat:wght@500&display=swap">
<style>
  :root {
    --backdrop: #000000;
    --card-light: #f3f3f3;
    --brand-blue: #1576c9;
    --blue-deep: #0b6fc4;
    --blue-soft: #2a88d6;
    --ink: #1e1e1e;
    --white: #ffffff;
  }
  * { margin: 0; padding: 0; box-sizing: border-box; }
  html, body {
    width: 1200px;
    height: 900px;
    overflow: hidden;
    background: var(--backdrop);
  }
  .canvas {
    position: relative;
    width: 1200px;
    height: 900px;
    background: var(--backdrop);
  }
  .card {
    position: absolute;
    top: 200px;
    width: 310px;
    height: 502px;
  }
  .card--front {
    left: 265px;
    background: var(--card-light);
    border-radius: 55px 0 55px 0;
  }
  .card--back {
    left: 641px;
    width: 309px;
    background: linear-gradient(160deg, var(--blue-soft) 0%, var(--blue-deep) 55%, #0a68b9 100%);
    border-radius: 0 55px 0 55px;
  }
  .wordmark {
    position: absolute;
    font-family: "Montserrat", sans-serif;
    font-weight: 500;
    text-align: center;
    line-height: 1;
  }
  .wordmark__name {
    display: block;
    font-size: 46px;
    letter-spacing: 3px;
  }
  .wordmark__field {
    display: block;
    font-size: 18px;
    letter-spacing: 5px;
    margin-top: 10px;
  }
  .card--front .wordmark {
    left: 0; right: 0;
    top: 145px;
    color: var(--brand-blue);
  }
  .card--back .wordmark {
    left: 0; right: 0;
    top: 250px;
    color: var(--white);
  }
  .contact {
    position: absolute;
    left: 25px;
    top: 320px;
    color: var(--ink);
    font-family: "Lato", sans-serif;
    font-size: 13.5px;
  }
  .contact__name {
    font-family: "Arimo", sans-serif;
    font-weight: 700;
    font-size: 18.5px;
    color: var(--brand-blue);
    line-height: 20px;
  }
  .contact__role {
    line-height: 18px;
    margin-bottom: 8px;
  }
  .contact__list { list-style: none; }
  .contact__item {
    display: flex;
    align-items: center;
    gap: 4px;
    line-height: 18px;
  }
  .contact__icon {
    width: 12px;
    height: 12px;
    fill: var(--brand-blue);
    flex: none;
  }
  .contact__address {
    margin-top: 7px;
    line-height: 18px;
    font-style: normal;
  }
</style>
</head>
<body>
<main class="canvas">
  <section class="card card--front" aria-label="Card front with contact details">
    <div class="wordmark">
      <span class="wordmark__name">HARBOR</span>
      <span class="wordmark__field">ADVERTISING</span>
    </div>
    <div class="contact">
      <p class="contact__name">MARCUS FELDON</p>
      <p class="contact__role">Managing Director</p>
      <ul class="contact__list">
        <li class="contact__item">
          <svg class="contact__icon" viewBox="0 0 24 24" aria-hidden="true"><path d="M6.6 10.8a15.2 15.2 0 0 0 6.6 6.6l2.2-2.2c.3-.3.7-.4 1-.2 1.1.4 2.3.6 3.6.6.6 0 1 .4 1 1V20c0 .6-.4 1-1 1A17 17 0 0 1 3 4c0-.6.4-1 1-1h3.5c.6 0 1 .4 1 1 0 1.3.2 2.5.6 3.6.1.3 0 .7-.2 1z"/></svg>
          <span>(044)123456789</span>
        </li>
        <li class="contact__item">
          <svg class="contact__icon" viewBox="0 0 24 24" aria-hidden="true"><path d="M2 5h20v14H2z M2 5l10 8 10-8" fill="var(--brand-blue)" stroke="var(--card-light)" stroke-width="1.6"/></svg>
          <span>info@youremail.com</span>
        </li>
        <li class="contact__item">
          <svg class="contact__icon" viewBox="0 0 24 24" aria-hidden="true"><circle cx="12" cy="12" r="10"/><path d="M2 12h20M12 2c3 3 3 17 0 20M12 2c-3 3-3 17 0 20" fill="none" stroke="var(--card-light)" stroke-width="1.4"/></svg>
          <span>www.websitename.com</span>
        </li>
      </ul>
      <address class="contact__address">1234, Address GoesHere,<br>Country name, 12345</address>
    </div>
  </section>

  <section class="card card--back" aria-label="Card back with company name">
    <div class="wordmark">
      <span class="wordmark__name">HARBOR</span>
      <span class="wordmark__field">ADVERTISING</span>
    </div>
  </section>
</main>
</body>
</html>
```